Lens Harbor Teutonia Website - Photography and Films

We are looking for a design that expresses the friendly, open nature of our company Lens Harbor Teutonia, yet at the same time is professional looking and functional.

Lens Harbor Teutonia is a B2B focused operation that hires out multi-lingual camera crews (and equipment) throughout Germany and Europe. We also produce tv features and coporate films. Our unique selling point is that we are native English speakers who can communicate with our international clients (usually British or American) and organise the logistics of shooting in foreign countries.

For content inspiration, see our current website: http://www.lensharborteutonia.com - however we want to move away from the very simple structure of this site and move towards a layout that displays and allows for frequently updated content (e.g. in the form of a blog).

Here is an example of the kind of clean look we like:
http://www.qrvpixelarchive.com/archive/main/reelsqrv.do#reel=48213760

Please keep within the following specifications:
- We wish to keep our logo (grey/white, font: Glypha) and our company colour red (#C40A0A) as they are.
- Maximum Width 960px, on a large browser-window the design should be centred
- Easily readable font sizes with good contrast
- Provide your design in PSD file format
- Our logo should be graphically displayed in the top left of the header.
- The design should allow space for a video.
- The page should have a clearly recognisable end in the form of a footer.

The following menu items need to be clearly arranged so the viewer is not overwhelmed or confused:
About
Services - Crews / Corporate Shoots / Webcasts / Production Arm / Legal Videography
Recent Productions
Blog
Testimonials
Get a Quote
Contact
Film Library
Showreel
Events
Film Location Guide - Frankfurt / Cologne / Zurich / Helsinki / Amsterdam / London / Paris / Rome / Brussels / Berlin / Munich
Updates

Reason: Hi - thanks very much for your interest in our design project.  We are extending this auction because we haven't had enough time to really focus on the desigs and provide immediate feedback to designers.  We will try to provide timely feedback and are giving you more time to make any adjustments to your designs etc.
Thanks!
Marla

Target Market(s)

Our target customers are males and females between 25 and 55 years (mostly British and American). More important than their demographic though, is their occupation - they are largely communication and design savvy individuals belonging to one of the following three categories: 1)Broadcasters (usually producers for example from the QRV or Horizon Vista TV seeking trustworthy, affordable crews for their foreign shoots).

2) Video Production Companies (seeking a trustworthy, affordable partner company to provide the crews for their own corporate clients).

3) Corporate Communications Specialists (seeking professional producers and crews to facilitate production of company videos or filming of events).

Industry/Entity Type

Camera

Requirements
Must have
• A fresh clean appearance with good use of white space.
Should not have
• Avoid dark heavy colours and designs.
• Avoid designs that would be impractical and could potentially take a long time to load.

```html
<!DOCTYPE html>
<html lang="en">
<head>
<meta charset="utf-8">
<title>Lens Harbor Teutonia</title>
<link rel="stylesheet" href="https://fonts.googleapis.com/css2?family=Arimo:wght@400;700&display=swap">
<style>
:root{
  --red:#c40a0a;
  --red-dark:#9a0606;
  --red-deep:#7e0303;
  --grey-line:#cfcfcf;
  --text:#333;
  --white:#fff;
}
*{margin:0;padding:0;box-sizing:border-box}
html,body{width:1200px;height:900px;overflow:hidden}
body{font-family:"Arimo",Arial,sans-serif;color:var(--text);position:relative;
  background:linear-gradient(#f6f6f6 0,#dcdcdc 330px,#fff 340px,#fff 100%)}
.topbar{position:absolute;left:0;top:0;width:1200px;height:16px;background:var(--red)}
.topbar-links{position:absolute;right:10px;top:2px;font-size:10px;font-weight:700;color:var(--white)}
.topbar-links span{margin:0 6px}
.logo{position:absolute;left:204px;top:62px;font-size:24px;font-weight:700;color:var(--red);letter-spacing:-1px;white-space:nowrap}
.logo-rule{position:absolute;left:204px;top:88px;width:252px;height:3px;background:var(--red)}
.nav{position:absolute;left:460px;top:56px;display:flex;height:36px;align-items:center;font-size:16px;color:#222}
.nav a{text-decoration:none;color:#222;margin-right:18px}
.nav .active{background:var(--red);color:var(--white);padding:9px 14px;border-radius:8px 8px 0 0;margin-right:16px;height:36px}
.hero{position:absolute;left:204px;top:88px;width:788px;height:306px;background:linear-gradient(#d20d0d,var(--red-dark));border-radius:10px 0 14px 14px}
.video{position:absolute;left:44px;top:36px;width:332px;height:258px;border-radius:10px;
  background:linear-gradient(135deg,#7ea06a,#3d4b36 55%,#1e1e1e);border:2px solid #b9b9b9}
.video svg{position:absolute;left:140px;top:100px}
.welcome{position:absolute;left:406px;top:28px;width:370px;color:var(--white)}
.welcome h1{font-size:27px;font-weight:700;margin-bottom:8px}
.welcome p{font-size:13.5px;line-height:16.5px}
.testimonial{position:absolute;left:400px;top:158px;width:364px;height:76px;background:var(--red-deep);border-radius:12px;padding:10px 50px 0 10px;color:var(--white)}
.testimonial h2{font-size:14px;font-style:italic;font-weight:400;margin-bottom:4px}
.testimonial p{font-size:10.5px;font-style:italic;font-weight:700;line-height:13px}
.testimonial svg{position:absolute;right:16px;top:24px}
.hero-buttons{position:absolute;left:402px;top:252px;display:flex;gap:6px}
.btn{background:var(--red-deep);color:var(--white);font-size:10.5px;font-weight:700;height:28px;line-height:28px;padding:0 14px;border-radius:6px}
.post{position:absolute;left:204px;width:472px;height:194px}
.post-date{position:absolute;left:0;top:0;width:44px;height:48px;background:var(--red);color:var(--white);text-align:center;font-weight:700}
.post-date .day{font-size:18px;line-height:26px}
.post-date .month{font-size:9px}
.post-card{position:absolute;left:44px;top:0;width:428px;height:194px;background:linear-gradient(#fff,#ececec);border:1px solid var(--grey-line);border-radius:0 16px 16px 16px;box-shadow:0 3px 5px rgba(0,0,0,.15);padding:8px 14px 0 20px}
.post-card h2{font-size:20px;color:var(--red);font-weight:400;margin-bottom:8px}
.post-card p{font-size:11px;line-height:12.5px;margin-bottom:10px}
.read-more{position:absolute;right:12px;bottom:8px;font-size:10px}
.divider{position:absolute;left:696px;top:410px;width:1px;height:420px;background:var(--grey-line)}
.side{position:absolute;left:714px;width:278px;height:196px;background:linear-gradient(#fff,#ececec);border:1px solid var(--grey-line);border-radius:16px;box-shadow:0 3px 5px rgba(0,0,0,.15);padding:6px 12px}
.side h2{font-size:20px;color:var(--red);font-weight:400;margin-bottom:8px}
.clients{display:grid;grid-template-columns:repeat(4,52px);gap:8px 6px}
.client{height:40px;background:var(--white);border:1px solid var(--grey-line);display:flex;align-items:center;justify-content:center;text-align:center;font-size:10px;font-weight:700;color:var(--text);line-height:11px}
.update{display:flex;align-items:center;margin-bottom:8px}
.avatar{width:40px;height:40px;border-radius:50%;background:linear-gradient(#f1c08a,#3a2a20);flex:none;margin-right:12px}
.update p{font-size:10.5px;font-style:italic;line-height:12px}
.footer{position:absolute;left:0;top:850px;width:1200px;height:50px;background:var(--red);color:var(--white);font-size:11px;font-weight:700;text-align:center;line-height:26px}
</style>
</head>
<body>
<div class="topbar"><div class="topbar-links"><span>Contact Us</span>|<span>About Us</span></div></div>

<div class="logo">lensharborteutonia</div>
<div class="logo-rule"></div>

<nav class="nav">
  <a class="active">Home</a><a>Services</a><a>Events</a><a>Film Library</a><a>Location Guide</a><a>Recent Poductions</a>
</nav>

<section class="hero">
  <div class="video" role="img" aria-label="Video still of a presenter being filmed in a studio">
    <svg width="52" height="52" viewBox="0 0 52 52"><circle cx="26" cy="26" r="25" fill="rgba(255,255,255,.35)"/><path d="M20 15 L38 26 L20 37Z" fill="rgba(255,255,255,.8)"/></svg>
  </div>
  <div class="welcome">
    <h1>Welcome!</h1>
    <p>30 years ago, Jonah Feldmark set up lens harbor teutonia to Fusce luctus leo vel est facilisis et pharetra turpis cursus. Cras ornare augue id mi cursus venenatis. Donec convallis tellus in lectus gravida pulvinar. In quis enim sapien, ut aliquam libero. Maecenas suscipit.</p>
  </div>
  <div class="testimonial">
    <h2>Testimonials</h2>
    <p>"Working with LHT on our corporate symposium shoots has always been a smooth partnership. Efficient, versatile and ever-helpful."</p>
    <svg width="18" height="28" viewBox="0 0 18 28"><path d="M3 2 L15 14 L3 26" fill="none" stroke="#fff" stroke-width="4"/></svg>
  </div>
  <div class="hero-buttons"><span class="btn">Get A Quote</span><span class="btn">Showreel</span><span class="btn">Our Blog</span></div>
</section>

<article class="post" style="top:412px">
  <div class="post-date"><div class="day">23</div><div class="month">OCT/10</div></div>
  <div class="post-card">
    <h2>Blog Post Example</h2>
    <p>Nam arcu libero, aliquet sit amet tristique vitae, imperdiet in risus. In orci eget urna faucibus lacinia aliquet eget est. Phasellus ullamcorper, lectus ultrices venenatis interdum, dui felis rhoncus dolor, commodo mollis magna felis eu nunc. Nunc rhoncus sem.</p>
    <p>Donec eleifend venenatis vulputate. Fusce a malesuada lacus. Maecenas tristique placerat risus, ac condimentum ipsum adipiscing sed. Phasellus augue lectus, mattis eget accumsan et, elementum non purus. Pellentesque habitant morbi tristique senectus et netus.</p>
    <span class="read-more">Read more...</span>
  </div>
</article>

<article class="post" style="top:636px">
  <div class="post-date"><div class="day">11</div><div class="month">OCT/10</div></div>
  <div class="post-card">
    <h2>Another Blog Post Example</h2>
    <p>Nam arcu libero, aliquet sit amet tristique vitae, imperdiet in risus. In orci eget urna faucibus lacinia aliquet eget est. Phasellus ullamcorper, lectus ultrices venenatis interdum, dui felis rhoncus dolor, commodo mollis magna felis eu nunc. Nunc rhoncus sem.</p>
    <p>Donec eleifend venenatis vulputate. Fusce a malesuada lacus. Maecenas tristique placerat risus, ac condimentum ipsum adipiscing sed. Phasellus augue lectus, mattis eget accumsan et, elementum non purus. Pellentesque habitant morbi tristique senectus et netus.</p>
    <span class="read-more">Read more...</span>
  </div>
</article>

<div class="divider"></div>

<aside class="side" style="top:410px">
  <h2>Clients</h2>
  <div class="clients">
    <div class="client">QRV</div><div class="client">Quadrant</div><div class="client">Orbis</div><div class="client">Horizon Vista TV</div>
    <div class="client">Tellux</div><div class="client">Pulse</div><div class="client">Peakcast</div><div class="client">Vantage</div>
    <div class="client">Meridian</div><div class="client">Terra Atlas</div><div class="client">Corvex</div><div class="client">Kairo</div>
  </div>
</aside>

<aside class="side" style="top:636px">
  <h2>Recent Additions</h2>
  <div class="update"><div class="avatar" role="img" aria-label="Profile picture of Tobias Renner"></div><p>Tobias Renner posted "Interesting blog post" on 20. July 2010.</p></div>
  <div class="update"><div class="avatar" role="img" aria-label="Profile picture of Helga Brandt"></div><p>Helga Brandt updated "Film Location Guide Berlin" on 18. July 2010.</p></div>
  <div class="update"><div class="avatar" role="img" aria-label="Profile picture of Jonah Feldmark"></div><p>Jonah Feldmark added a new client testimonial on 20. July 2010.</p></div>
</aside>

<footer class="footer">© 2010 Lens Harbor Teutonia | Feldmark Films GmbH. Frankfurt. Germany.</footer>
</body>
</html>
```